A new website for Electrical Contractor Business

We are looking for a unique and new WordPress website design which would include 5 Pages - Home Page, Meet the Team, Our Services, Our Projects and Contact Us page.

The global theme for the website needs to be professional but simple to navigate as we cater for both business and home owner customers.

Our core business service is targeted around lighting from single room decorative to large office so the theme should incorporate this in some way.

The home page should include;
Our business logo, Contact number, Email address, small Image rotation box - Highlighting pervious projectsText box - With welcome message, chirpnet feed news reel/Customer feed back box.

I would also like to see a 2 boxes for the separate customer types we services. Business and Home Owner. each box will have a small image with a small text description with a link to the area of the services page relevant to that customer type.

Meet the team page -This will be introducing potential customers to the team so I would like it to include for each team member. Something like a small image and text area which will introduce an outline of the team members skills and abilities.

Our Services page This page will be outlining the different services on offer to the both customer types business and homeowner. Each service should have an image with text description of the service would good here.

Our projects page-Will include images of pervious projects and work we have completed along with a text area for the project description/ outliner.

Contact Us page - Should include a contact form which should include an option for the customer to quest us to call them back, also a selection box for them to inform us our how they found our details would be good.

Colour - The theme colours can be taken from the logo or feel free to impress with your own imagination.

Remember we are looking for a website that will interest our customers enough to except our services or be drawn further into the website.. So call to action links to other areas of the site/ contact page are welcome

Target Market(s)

Business - Office, warehousing and Large Store - lighting and Power
Home owner lighting and power

Coding

Coded - Design and coding required

Number of Pages Required

5+ page

Font styles to use
Serif
Sans Serif

Colors

Designer to choose colors to be used in the design.

Requirements
Must have
• Logo integrated into the website design - i.e. website colours which allow the logo to blend into the design.
Nice to have
• Custom but professional theme catering to business customers, but also show that we do provide services to home owners too.
Should not have
• Sorry am not interested in one oversized block image on rotation covering half the home page.. Images will be needed but not a single block over sized frame with not text, shape. Please use your imagination when considering this design

```html
<!DOCTYPE html>
<html lang="en">
<head>
<meta charset="utf-8">
<title>Brightline Electrical</title>
<link href="https://fonts.googleapis.com/css2?family=Raleway:wght@400;600;700;800&family=Open+Sans:wght@400;600;700&display=swap" rel="stylesheet">
<style>
:root{
  --navy:#1f2f5c;
  --navy-dark:#1a2850;
  --orange:#f26a22;
  --orange-light:#f7a26f;
  --ink:#333a4a;
  --muted:#6b7280;
  --line:#d9dce3;
  --soft:#f4f3f4;
  --white:#ffffff;
}
*{margin:0;padding:0;box-sizing:border-box}
html,body{width:1200px;height:3913px;overflow:hidden}
body{position:relative;font-family:"Open Sans",Arial,sans-serif;color:var(--ink);background:var(--white);font-size:13px}
.abs{position:absolute}
h1,h2,h3,h4{font-family:"Raleway",Arial,sans-serif}

/* top bar */
.topbar{left:0;top:0;width:1200px;height:36px;background:var(--navy);color:var(--white);font-size:11px;font-weight:600}
.topbar .mail{left:172px;top:10px;display:flex;gap:6px;align-items:center}
.topbar .call{left:610px;top:0;width:230px;height:36px;background:var(--orange);clip-path:polygon(6% 0,100% 0,94% 100%,0 100%);display:flex;align-items:center;justify-content:center;gap:6px}
.topbar .web{left:858px;top:10px;display:flex;gap:6px;align-items:center}

/* header */
.header{left:0;top:36px;width:1200px;height:74px;background:var(--white)}
.brand{left:172px;top:12px;display:flex;align-items:center;gap:12px}
.brand .mark{width:50px;height:50px;border-radius:50%;background:var(--orange)}
.brand .name{font-family:"Raleway",sans-serif;font-weight:700;font-size:20px;color:var(--navy);letter-spacing:1px;line-height:1}
.nav{right:172px;top:29px;display:flex;gap:34px;font-family:"Raleway",sans-serif;font-weight:700;font-size:12px;color:var(--navy)}
.nav .active{color:var(--orange)}

/* hero */
.hero{left:0;top:110px;width:1200px;height:470px;background:linear-gradient(100deg,#f4f5f7 0%,#eceef1 35%,#c9ccd2 58%,#dfe2e6 78%,#f3f4f5 100%)}
.hero-copy{left:172px;top:160px;width:470px}
.hero-copy .kicker{font-family:"Raleway",sans-serif;font-weight:700;font-size:13px;color:var(--orange);letter-spacing:2px}
.hero-copy h2{margin-top:10px;font-weight:800;font-size:38px;line-height:1.15;color:var(--navy)}
.hero-copy p{margin-top:14px;font-size:13px;line-height:1.6;color:var(--ink);width:420px}
.hero-copy .btn{margin-top:20px;width:170px;height:42px;font-size:12px}
.dots{left:1000px;top:392px;display:flex;gap:8px}
.dots i{width:10px;height:10px;border-radius:50%;background:var(--white);border:1.5px solid var(--navy);display:block}
.dots i.on{background:var(--orange);border-color:var(--orange)}

/* customer types */
.type{top:428px;width:418px;height:130px;background:var(--white);border-top:3px solid var(--orange);box-shadow:0 6px 18px rgba(31,47,92,.14);display:flex;gap:18px;padding:14px}
.type .thumb{width:120px;height:100px;flex:none}
.type h3{font-weight:800;font-size:17px;color:var(--navy)}
.type p{margin-top:6px;font-size:11px;line-height:1.5;color:var(--muted)}
.type .link{display:inline-block;margin-top:8px;font-family:"Raleway",sans-serif;font-weight:700;font-size:11.5px;color:var(--orange)}

/* section titles */
.eyebrow{font-family:"Raleway",sans-serif;color:var(--orange);font-size:14px;font-weight:600;text-align:center;width:1200px;left:0}
.title{font-family:"Raleway",sans-serif;color:var(--navy);font-weight:800;font-size:34px;text-align:center;width:1200px;left:0;letter-spacing:.5px}
.rule{left:580px;width:40px;height:3px;background:var(--orange)}
.lede{width:1200px;left:0;text-align:center;font-size:12px;color:var(--ink)}

/* welcome */
.welcome-photo{left:172px;top:765px;width:345px;height:305px;background:linear-gradient(160deg,#e9ecef,#c8ccd3 50%,#34395a 75%,#d7dadf)}
.welcome-text{left:577px;top:790px;width:451px;font-size:11.5px;line-height:1.65;color:var(--muted)}
.ticks{left:577px;top:878px;list-style:none;font-size:11.5px;color:var(--muted)}
.ticks li{display:flex;align-items:center;gap:10px;margin-bottom:8px}
.btn{display:inline-flex;align-items:center;justify-content:center;background:var(--orange);color:var(--white);font-family:"Raleway",sans-serif;font-weight:700;border-radius:30px}
.btn-lg{left:577px;top:985px;width:135px;height:40px;font-size:12px}

/* services */
.services{left:0;top:1128px;width:1200px;height:738px;background:linear-gradient(90deg,#f1f2f4 0%,#f6f6f7 40%,#e7e8eb 70%,#d9dce1 100%)}
.card{width:272px;height:196px;border:1.5px solid var(--orange-light);background:rgba(255,255,255,.55);text-align:center}
.card .icon{position:absolute;left:101px;top:-32px;width:70px;height:70px;border-radius:50%;border:2px solid var(--orange-light);background:var(--white);display:flex;align-items:center;justify-content:center}
.card h3{margin-top:50px;font-family:"Open Sans",sans-serif;font-weight:400;font-size:16px;color:var(--ink)}
.card p{margin:12px auto 0;width:215px;font-size:10.5px;line-height:1.45;color:var(--muted)}
.card .btn{position:absolute;left:86px;bottom:22px;width:100px;height:30px;font-size:10px}

/* team */
.team{left:0;top:2474px;width:1200px;height:541px;background:var(--soft)}
.member{width:200px;height:314px}
.member .photo{width:100%;height:238px;background:linear-gradient(180deg,#e8eaed 0%,#cfd3d9 55%,#22263a 100%)}
.member .label{width:100%;height:76px;background:var(--orange);color:var(--white);text-align:center;padding-top:18px}
.member .label h4{font-family:"Open Sans",sans-serif;font-weight:700;font-size:15px}
.member .label span{font-size:10.5px}

/* cta */
.cta{left:0;top:3015px;width:1200px;height:110px;background:linear-gradient(90deg,#23346a,#2b3f78 60%,#22336a)}
.cta .msg{left:172px;top:32px;width:250px;color:var(--white);font-size:11.5px;line-height:1.55}
.cta .phone{left:520px;top:26px;display:flex;gap:16px;align-items:center;color:var(--white)}
.cta .phone small{font-size:14px;display:block}
.cta .phone strong{font-size:24px;font-family:"Raleway",sans-serif;font-weight:700}
.cta .call-btn{left:865px;top:37px;width:148px;height:38px;border:2px solid var(--white);border-radius:30px;color:var(--white);font-family:"Raleway",sans-serif;font-weight:700;font-size:13px;display:flex;align-items:center;justify-content:center}

/* contact */
.contact-info{left:172px;top:3336px}
.info{display:flex;gap:18px;margin-bottom:32px}
.info h5{font-size:11px;font-weight:700;color:var(--ink)}
.info p{font-size:10.5px;color:var(--muted);line-height:1.5}
.field{height:38px;border:1px solid var(--line);font-size:10.5px;color:#9aa0aa;padding:11px 14px;background:var(--white)}
.submit{left:472px;top:3544px;width:115px;height:36px;font-size:13px}

/* footer */
.footer{left:0;top:3647px;width:1200px;height:266px;background:var(--navy-dark);color:var(--white)}
.footer h4{font-family:"Raleway",sans-serif;font-size:15px;font-weight:700;letter-spacing:.5px}
.footer p,.footer li{font-size:11px;line-height:1.55}
.links{list-style:none}
.links li{margin-bottom:8px;display:flex;gap:10px}
.bottom{left:172px;width:856px;height:38px;background:var(--orange);border-radius:20px;font-size:10.5px;display:flex;align-items:center;justify-content:space-between;padding:0 22px}
.socials{display:flex;gap:7px;align-items:center}
.socials i{width:16px;height:16px;background:var(--white);border-radius:2px;display:block}
</style>
</head>
<body>

<!-- Top bar -->
<div class="abs topbar">
  <div class="abs mail"><svg width="12" height="9" viewBox="0 0 12 9"><rect x=".5" y=".5" width="11" height="8" fill="none" stroke="#fff"/><path d="M.5 .5 6 5l5.5-4.5" fill="none" stroke="#fff"/></svg>hello@brightline-electric.example</div>
  <div class="abs call"><svg width="11" height="11" viewBox="0 0 24 24"><path fill="#fff" d="M6.6 10.8a15 15 0 0 0 6.6 6.6l2.2-2.2c.3-.3.7-.4 1-.2 1.1.4 2.3.6 3.6.6.6 0 1 .4 1 1V20c0 .6-.4 1-1 1A17 17 0 0 1 3 4c0-.6.4-1 1-1h3.5c.6 0 1 .4 1 1 0 1.3.2 2.5.6 3.6.1.3 0 .7-.2 1z"/></svg>Call to us : +61 5550 123 987</div>
  <div class="abs web"><svg width="11" height="11" viewBox="0 0 24 24"><circle cx="12" cy="12" r="10" fill="none" stroke="#fff" stroke-width="2"/><path d="M2 12h20M12 2c3 3 3 17 0 20M12 2c-3 3-3 17 0 20" fill="none" stroke="#fff" stroke-width="1.5"/></svg>www.brightline-electric.example</div>
</div>

<!-- Header -->
<header class="abs header">
  <div class="abs brand"><span class="mark"></span><span class="name">BRIGHTLINE ELECTRICAL</span></div>
  <nav class="abs nav"><span class="active">HOME</span><span>MEET THE TEAM</span><span>OUR SERVICES</span><span>PROJECTS</span><span>CONTACT US</span></nav>
</header>

<!-- Hero with rotating project slides -->
<div class="abs hero" role="img" aria-label="Electrician in blue overalls and hard hat wiring a wall outlet beside a stepladder in a bright room"></div>
<div class="abs hero-copy">
  <div class="kicker">LIGHTING &amp; POWER</div>
  <h2>Lighting for Every Space, Office to Living Room</h2>
  <p>From a single decorative room to a large office floor, we plan, install and maintain lighting and power.</p>
  <a class="btn">GET A FREE QUOTE</a>
</div>
<div class="abs dots"><i class="on"></i><i></i><i></i></div>

<!-- Customer types -->
<div class="abs type" style="left:172px">
  <div class="thumb" role="img" aria-label="Bright office floor with ceiling lighting" style="background:linear-gradient(160deg,#f1f2f3,#c9ccd1 55%,#6d7078)"></div>
  <div><h3>Business</h3><p>Offices, warehousing and large stores — lighting and power planned around your work.</p><a class="link">Business services ›</a></div>
</div>
<div class="abs type" style="left:610px">
  <div class="thumb" role="img" aria-label="Warm living room lit by pendant lamps" style="background:linear-gradient(160deg,#f6eee4,#e1c7a6 55%,#8a6a4c)"></div>
  <div><h3>Home Owner</h3><p>Decorative room lighting, new outlets and safe wiring for your home, done right.</p><a class="link">Home services ›</a></div>
</div>

<!-- Welcome -->
<div class="abs eyebrow" style="top:628px">WELCOME TO</div>
<h1 class="abs title" style="top:644px">BRIGHTLINE ELECTRICAL</h1>
<div class="abs rule" style="top:690px"></div>
<p class="abs lede" style="top:700px">Lorem ipsum dolor sit amet consectetur adipiscing elit sed do eiusm tempor</p>

<div class="abs welcome-photo" role="img" aria-label="Smiling electrician in orange hard hat and work jacket with arms crossed"></div>
<p class="abs welcome-text">Excepteur sint occaecat cupidatat non proident, sunt in culpa qui officia deserunt mollit anim id est laborum. Sed ut perspiciatis unde omnis natus error sit voluptatem accusantium doloremque laudantium totam rem aperiam eaque ipsa quae ab illo inventore veritatis et quasi architecto beatae vitae dicta sunt explicabo.</p>
<ul class="abs ticks">
  <li><svg width="14" height="14" viewBox="0 0 14 14"><rect width="14" height="14" rx="2" fill="#f26a22"/><path d="M3.5 7.2 6 9.6l4.6-5" fill="none" stroke="#fff" stroke-width="1.8"/></svg>Morbi fermentum felis nec</li>
  <li><svg width="14" height="14" viewBox="0 0 14 14"><rect width="14" height="14" rx="2" fill="#f26a22"/><path d="M3.5 7.2 6 9.6l4.6-5" fill="none" stroke="#fff" stroke-width="1.8"/></svg>Morbi fermentum felis nec gravida tempus.</li>
  <li><svg width="14" height="14" viewBox="0 0 14 14"><rect width="14" height="14" rx="2" fill="#f26a22"/><path d="M3.5 7.2 6 9.6l4.6-5" fill="none" stroke="#fff" stroke-width="1.8"/></svg>Morbi fermentum felis nec gravida</li>
</ul>
<a class="abs btn btn-lg">READ MORE</a>

<!-- Services -->
<section class="abs services" role="img" aria-label="Faded background of an electrician working on cabling"></section>
<div class="abs eyebrow" style="top:1174px">BRIGHTLINE ELECTRICAL</div>
<h2 class="abs title" style="top:1188px">OUR SERVICES</h2>
<div class="abs rule" style="top:1234px"></div>
<p class="abs lede" style="top:1246px">Lorem ipsum dolor sit amet consectetur adipiscing elit sed do eiusm tempor</p>

<div class="abs card" style="left:172px;top:1331px">
  <div class="icon"><svg width="30" height="30" viewBox="0 0 30 30" fill="none" stroke="#f26a22" stroke-width="2"><path d="M20 4l6 6-13 13-7 1 1-7z"/><path d="M17 7l6 6"/></svg></div>
  <h3>Light Setting</h3><p>Lorem ipsum dolor sit amet conctur adipising slit sed do eiusmtempor incid dolore magna aliqu enim ad.</p><a class="btn">READ MORE</a></div>
<div class="abs card" style="left:465px;top:1331px">
  <div class="icon"><svg width="32" height="30" viewBox="0 0 32 30" fill="none" stroke="#f26a22" stroke-width="2"><rect x="7" y="5" width="18" height="10" rx="2"/><rect x="3" y="13" width="26" height="8" rx="2"/><path d="M6 21v4M26 21v4"/></svg></div>
  <h3>Room Decoration</h3><p>Lorem ipsum dolor sit amet conctur adipising slit sed do eiusmtempor incid dolore magna aliqu enim ad.</p><a class="btn">READ MORE</a></div>
<div class="abs card" style="left:757px;top:1331px">
  <div class="icon"><svg width="32" height="30" viewBox="0 0 32 30" fill="none" stroke="#f26a22" stroke-width="2"><circle cx="11" cy="7" r="4"/><path d="M5 24v-8h9l3 6h10M17 16h12v10M8 16v10"/></svg></div>
  <h3>Large Office Setting</h3><p>Lorem ipsum dolor sit amet conctur adipising slit sed do eiusmtempor incid dolore magna aliqu enim ad.</p><a class="btn">READ MORE</a></div>
<div class="abs card" style="left:172px;top:1603px">
  <div class="icon"><svg width="30" height="30" viewBox="0 0 30 30" fill="none" stroke="#f26a22" stroke-width="2"><path d="M10 19a8 8 0 1 1 10 0v3H10z"/><path d="M11 26h8M13 15l2-3 2 3"/></svg></div>
  <h3>Electrical Maintenance</h3><p>Lorem ipsum dolor sit amet conctur adipising slit sed do eiusmtempor incid dolore magna aliqu enim ad.</p><a class="btn">READ MORE</a></div>
<div class="abs card" style="left:465px;top:1603px">
  <div class="icon"><svg width="30" height="30" viewBox="0 0 30 30" fill="none" stroke="#f26a22" stroke-width="2"><path d="M15 4l12 21H3z"/><path d="M15 12v6M15 21v1"/></svg></div>
  <h3>Sefty Services</h3><p>Lorem ipsum dolor sit amet conctur adipising slit sed do eiusmtempor incid dolore magna aliqu enim ad.</p><a class="btn">READ MORE</a></div>
<div class="abs card" style="left:757px;top:1603px">
  <div class="icon"><svg width="32" height="30" viewBox="0 0 32 30" fill="none" stroke="#f26a22" stroke-width="2"><rect x="4" y="5" width="24" height="16" rx="1"/><path d="M12 26h8M16 21v5M11 13l4 3 6-6"/></svg></div>
  <h3>Installation</h3><p>Lorem ipsum dolor sit amet conctur adipising slit sed do eiusmtempor incid dolore magna aliqu enim ad.</p><a class="btn">READ MORE</a></div>

<!-- Projects -->
<div class="abs eyebrow" style="top:1910px">OUR</div>
<h2 class="abs title" style="top:1922px">PROJECTS</h2>
<div class="abs rule" style="top:1968px"></div>
<p class="abs lede" style="top:1980px">Lorem ipsum dolor sit amet consectetur adipiscing elit sed do eiusm tempor</p>

<div class="abs" style="left:172px;top:2041px;width:272px;height:358px;background:linear-gradient(180deg,#f0f1f2,#d5d8dc 45%,#5b5e63 75%,#9a9ea3)" role="img" aria-label="Empty modern office with rows of black chairs and large windows"></div>
<div class="abs" style="left:465px;top:2041px;width:271px;height:167px;background:linear-gradient(135deg,#cfd3d8,#c6863f 45%,#8d7b6c 70%,#dfe1e4)" role="img" aria-label="Electrician in yellow hard hat fitting a ceiling light"></div>
<div class="abs" style="left:757px;top:2041px;width:271px;height:167px;background:linear-gradient(135deg,#eceeef,#d6d8db 50%,#3a3c41 80%,#e1b236)" role="img" aria-label="Electrician in hard hat adjusting a ceiling lamp"></div>
<div class="abs" style="left:465px;top:2228px;width:271px;height:171px;background:linear-gradient(135deg,#3b6fb6,#d4a37f 40%,#5f8fcf 70%,#2f5fa6)" role="img" aria-label="Technician in blue shirt working on an electrical panel"></div>
<div class="abs" style="left:757px;top:2228px;width:271px;height:171px;background:linear-gradient(180deg,#f3f3f3,#dcdcdb 50%,#b9b6b1 80%,#e6e5e3)" role="img" aria-label="Bright open office interior with pendant lighting"></div>

<!-- Team -->
<section class="abs team"></section>
<div class="abs eyebrow" style="top:2520px">OUR</div>
<h2 class="abs title" style="top:2532px">MEET THE TEAM</h2>
<div class="abs rule" style="top:2578px"></div>

<div class="abs member" style="left:172px;top:2620px"><div class="photo" role="img" aria-label="Portrait of a team member in a dark business suit"></div><div class="label"><h4>MARA QUINLAN</h4><span>Lorem ipsum</span></div></div>
<div class="abs member" style="left:394px;top:2620px"><div class="photo" role="img" aria-label="Portrait of a team member in a dark business suit"></div><div class="label"><h4>OWEN HARTLEY</h4><span>Lorem ipsum</span></div></div>
<div class="abs member" style="left:613px;top:2620px"><div class="photo" role="img" aria-label="Portrait of a team member in a dark business suit"></div><div class="label"><h4>FELIX MARLOW</h4><span>Lorem ipsum</span></div></div>
<div class="abs member" style="left:833px;top:2620px"><div class="photo" role="img" aria-label="Portrait of a team member in a dark business suit"></div><div class="label"><h4>LENA BROOKS</h4><span>Lorem ipsum</span></div></div>

<!-- CTA band -->
<section class="abs cta">
  <p class="abs msg">Come aboard were expecting you. Love life's sweet-est reward Let it flow it floats back to you?</p>
  <div class="abs phone">
    <svg width="54" height="54" viewBox="0 0 24 24"><path fill="none" stroke="#fff" stroke-width="1.2" d="M6.6 10.8a15 15 0 0 0 6.6 6.6l2.2-2.2c.3-.3.7-.4 1-.2 1.1.4 2.3.6 3.6.6.6 0 1 .4 1 1V20c0 .6-.4 1-1 1A17 17 0 0 1 3 4c0-.6.4-1 1-1h3.5c.6 0 1 .4 1 1 0 1.3.2 2.5.6 3.6.1.3 0 .7-.2 1z"/><path fill="none" stroke="#fff" stroke-width="1.2" d="M14 3a7 7 0 0 1 7 7M14 6a4 4 0 0 1 4 4"/></svg>
    <div><small>Get Free Consultation</small><strong>+ 61 5550 123 987</strong></div>
  </div>
  <div class="abs call-btn">CALL US NOW</div>
</section>

<!-- Contact -->
<div class="abs eyebrow" style="top:3154px">OUR</div>
<h2 class="abs title" style="top:3166px">CONTACT US</h2>
<div class="abs rule" style="top:3212px"></div>
<p class="abs lede" style="top:3238px;left:270px;width:660px;line-height:1.6;font-size:11px">Dummy text is also used to demonstrate the appearance of different typefaces and layouts, and in general the content of dummy text is nonsensical. Due to its widespread use as filler text for layouts. Dummy text is also used to demonstrate the</p>

<div class="abs contact-info">
  <div class="info"><svg width="16" height="20" viewBox="0 0 16 20"><path fill="#f26a22" d="M8 0a8 8 0 0 0-8 8c0 6 8 12 8 12s8-6 8-12a8 8 0 0 0-8-8zm0 11a3 3 0 1 1 0-6 3 3 0 0 1 0 6z"/></svg><div><h5>ADDRESS</h5><p>418 Harbour Lane Westfield, Canada.</p></div></div>
  <div class="info"><svg width="18" height="14" viewBox="0 0 18 14"><rect width="18" height="14" rx="1" fill="#f26a22"/><path d="M1 1l8 6 8-6" fill="none" stroke="#fff" stroke-width="1.4"/></svg><div><h5>MAIL</h5><p>hello@brightline-electric.example</p></div></div>
  <div class="info"><svg width="16" height="16" viewBox="0 0 24 24"><path fill="#f26a22" d="M6.6 10.8a15 15 0 0 0 6.6 6.6l2.2-2.2c.3-.3.7-.4 1-.2 1.1.4 2.3.6 3.6.6.6 0 1 .4 1 1V20c0 .6-.4 1-1 1A17 17 0 0 1 3 4c0-.6.4-1 1-1h3.5c.6 0 1 .4 1 1 0 1.3.2 2.5.6 3.6.1.3 0 .7-.2 1z"/></svg><div><h5>PHONE</h5><p>+ 61 5550 123 987</p></div></div>
</div>

<div class="abs field" style="left:472px;top:3336px;width:270px">Name</div>
<div class="abs field" style="left:757px;top:3336px;width:271px">Last Name</div>
<div class="abs field" style="left:472px;top:3388px;width:270px">E-Mail</div>
<div class="abs field" style="left:757px;top:3388px;width:271px">Phone</div>
<div class="abs field" style="left:472px;top:3440px;width:556px;height:82px">Message</div>
<a class="abs btn submit">SUBMIT</a>

<!-- Footer -->
<footer class="abs footer">
  <div class="abs" style="left:172px;top:44px;width:230px">
    <h4>ABOUT US</h4>
    <p style="margin-top:12px">Lorem Ipsum has been the industry's standard dummy text ever since the 1500s, when an unknown printer took a galley of type and scrambled it to make a type specimen book. It has survived not only five centuries.</p>
  </div>
  <div class="abs" style="left:488px;top:44px;width:260px">
    <h4>USEFULL LINKS</h4>
    <div style="display:flex;gap:60px;margin-top:14px">
      <ul class="links"><li>›&nbsp; Home</li><li>›&nbsp; Meet the Team</li><li>›&nbsp; Our Services</li></ul>
      <ul class="links"><li>›&nbsp; Projects</li><li>›&nbsp; Contact Us</li></ul>
    </div>
  </div>
  <div class="abs" style="left:770px;top:36px;width:258px">
    <div style="display:flex;align-items:center;gap:12px;border-bottom:1px solid rgba(255,255,255,.5);padding-bottom:8px">
      <span style="width:34px;height:34px;border:1.5px solid #fff;border-radius:50%;display:block"></span>
      <h4>CHIRPNET</h4>
    </div>
    <div style="display:flex;gap:12px;margin-top:14px">
      <span role="img" aria-label="Small profile avatar" style="width:38px;height:38px;border-radius:50%;background:linear-gradient(135deg,#b9a28c,#5d4b3e);flex:none"></span>
      <p>Lorem ipsum: or ipsum as it is sometimes known, is dummy.<br><span style="color:#7fb2ff">@ chirpnet</span></p>
    </div>
  </div>
  <div class="abs bottom" style="top:205px">
    <span>© 2019 Brightline Electrical . All Right Reserved.</span>
    <span class="socials">Follow Us : <i></i><i></i><i></i></span>
  </div>
</footer>

</body>
</html>
```